Luxury Home Builder looking for an Exciting Homes Portfolio

We have a number of custom homes that we have completed over the years, and we want to give prospective clients are colorful and exciting catalog of our previous homes. I will provide access to the dropbox with all the photos. Need to get as many photos of homes in the catalog as possible. Please use talvinecrestbuilds.com for pictures, lots of them in the portfolio, projects in progress, spec homes are available. I will provide full files to the winner. Need a very hip catalog to give out at events, and marketing venues.

Target Market(s)

High Net Worth Individuals looking for luxury homes

Industry/Entity Type

Real Estate Development

Requirements
Must have
• Photos of our project, please use talvinecrestbuilds.com to get the photos, and will provide access to full pictures on dropbox to the winner.
• Logo must be incorporated.
Nice to have
• Clarification, website is not for design, but for the purposes of getting the photos. this has to be a very cool portfolio.

```html
<!DOCTYPE html>
<html lang="en">
<head>
<meta charset="utf-8">
<title>Talvinecrest Builds — Who We Are</title>
<link rel="stylesheet" href="https://fonts.googleapis.com/css2?family=Open+Sans:wght@400;700&display=swap">
<style>
  :root {
    --canvas: #e9e4dc;
    --navy: #23446b;
    --red: #b8201e;
    --white: #ffffff;
    --photo-light: #d3e4f0;
    --photo-deep: #6cc2dc;
    --edge-light: #e6eaec;
    --edge-deep: #b9bcae;
  }
  html, body {
    margin: 0;
    width: 1200px;
    height: 1200px;
    overflow: hidden;
    background: var(--canvas);
  }
  .page {
    position: absolute;
    left: 159px;
    top: 30px;
    width: 881px;
    height: 1140px;
    display: flex;
    box-shadow: 0 4px 14px rgba(0,0,0,0.25);
  }
  .page__photo {
    width: 389px;
    height: 100%;
    background: linear-gradient(180deg, var(--photo-light) 0%, var(--photo-deep) 100%);
  }
  .page__content {
    position: relative;
    width: 441px;
    height: 100%;
    background: var(--navy);
    box-sizing: border-box;
    padding: 50px 52px 0 52px;
    font-family: "Open Sans", sans-serif;
    color: var(--white);
  }
  .page__edge-photo {
    width: 51px;
    height: 100%;
    background: linear-gradient(180deg, var(--edge-light) 0%, var(--edge-deep) 100%);
  }
  .section-title {
    margin: 0 0 26px 0;
    font-size: 20px;
    font-weight: 700;
    letter-spacing: 0.2px;
  }
  .section-body {
    margin: 0;
    font-size: 16.5px;
    line-height: 23.5px;
    text-align: justify;
  }
  .section + .section {
    margin-top: 44px;
  }
  .accent-band {
    position: absolute;
    left: 0;
    bottom: 0;
    width: 100%;
    height: 51px;
    background: var(--red);
  }
</style>
</head>
<body>
  <div class="page">
    <div class="page__photo" role="img" aria-label="Photo of a white Mediterranean-style luxury home with palm trees and a large swimming pool"></div>
    <div class="page__content">
      <section class="section">
        <h2 class="section-title">WHO WE ARE</h2>
        <p class="section-body">At Talvinecrest, there are no easy answers, no pat formulas. We leave that sort of thing to the mass market developers. Each home we undertake is a one-of-a-kind, fully customized residence, designed to meet the specific desires of its residents. When you work with a limited universe of prospective clients, there is no room for error. Every home we Design-Build must measure up on every count. Because we know that our clients, our homebuyers, serve as our salespeople. Indeed, they are the only 'sales force' we have. They're the best measure of how well we deliver on our promises. We urge anyone interested in the prospect of working with us, to talk to those who have relied on us in the past to create their homes.</p>
      </section>
      <section class="section">
        <h2 class="section-title">OUR GOAL</h2>
        <p class="section-body">Talvinecrest Builds, Inc. is different from other builders because we are a Design-Build company, where every project we undertake is centered on the principle of listening to our clients in order to understand their needs, and on honesty and transparency from start to finish. We take the time to listen to our clients in order to create a custom home that is true to their vision. Talvinecrest team works with our clients in open collaboration on every aspect of the build. Every Talvinecrest home is a statement about who our clients are and about who we are.</p>
      </section>
      <div class="accent-band"></div>
    </div>
    <div class="page__edge-photo" role="img" aria-label="Edge of a neighbouring photo of a garden and stone walkway"></div>
  </div>
</body>
</html>
```